Website design for recruitment solutions

We connect top talents to fast growing employers in Asia. We need to revamp our existing website (currently outdated) and also add more pages to make it more informative for talents and employers.
We need final design output to be for both desktop and mobile devices. The final design output must come with all specifications so it's easier for our dev team to implement. We have a detailed mockup but we expect the design to be significantly changed by the final output. We want the pages to look aesthetic, modern and professional.
Number of Pages Required
5+ page
Requirements
Must have
- - To have Pages design for desktop+mobile. Need to take into account intermediate resolutions like 1365px\1023px\767px\479px, especially if mobile/desktop design differs considerably. Design should be repeatable (between pages), suitable for block-layout.
Nice to have
- In terms of receiving files, we usually work with designers who can deliver files in Figma or Sketch with export to Figma. If in PSD format - please export to Zeplin or Avocode, otherwise will be difficult to open

```html
<!DOCTYPE html>
<html lang="en">
<head>
<meta charset="utf-8">
<title>Vantira — How we grew</title>
<link href="https://fonts.googleapis.com/css2?family=Roboto:wght@400;500;700;900&display=swap" rel="stylesheet">
<style>
:root{
  --brand:#5874a0;
  --brand-light:#a9c0e3;
  --red:#ff0808;
  --green:#6cc99a;
  --title:#4f6b9a;
  --ink:#333;
  --page:#f8f8f8;
  --white:#fff;
}
*{box-sizing:border-box;margin:0;padding:0}
html,body{width:834px;height:1200px;overflow:hidden}
body{position:relative;background:var(--page);font-family:'Roboto',sans-serif;color:var(--ink)}
.abs{position:absolute}

/* hero */
.hero{position:absolute;left:0;top:0;width:834px;height:338px;overflow:hidden}
.hero-photo{position:absolute;inset:0;background:linear-gradient(180deg,#8e9398 0%,#8a9096 22%,#6f7a80 40%,#5c6166 65%,#4a4d52 100%)}
.hero-wave{position:absolute;left:0;bottom:0;width:834px;height:44px}
.hero-title{position:absolute;left:0;width:834px;top:168px;text-align:center;color:var(--white);font-weight:900;font-size:22.5px;line-height:27px;letter-spacing:-.1px}
.hero-title .accent{color:var(--red)}

/* nav */
.nav{position:absolute;left:176px;top:0;width:482px;height:27px;background:var(--brand);border-radius:0 0 12px 12px;box-shadow:0 3px 6px rgba(0,0,0,.18)}
.logo{position:absolute;font-weight:700;letter-spacing:1.2px;color:var(--brand-light)}
.nav .logo{left:13px;top:8px;font-size:10px}
.nav-link{position:absolute;top:10px;font-size:5.2px;color:var(--white)}
.nav-link.active::after{content:"";position:absolute;left:-5px;right:-5px;top:16px;height:1px;background:var(--red)}
.nav-divider{position:absolute;left:387px;top:9px;width:.6px;height:9px;background:var(--white)}
.btn-register{position:absolute;background:var(--red);color:var(--white);border-radius:7px;font-size:5.2px;display:flex;align-items:center;justify-content:center;gap:2px}
.btn-register .doc{width:3.5px;height:4.5px;background:var(--white);border-radius:.5px}
.login-dot{display:inline-block;width:5px;height:5px;border:.8px solid var(--white);border-radius:50%;vertical-align:-1px;margin-right:1.5px}

/* tabs */
.tab{position:absolute;top:386px;height:26px;display:flex;align-items:center;justify-content:center;font-size:16px;font-weight:700;color:var(--title);background:#f1f1f1;border:1px solid #ddd;border-bottom:none;border-radius:4px 4px 0 0}
.tab.active{background:var(--brand);color:var(--white);border-color:var(--brand)}
.panel{position:absolute;left:176px;top:412px;width:482px;height:546px;background:var(--white);box-shadow:0 1px 4px rgba(0,0,0,.12);border-radius:0 0 3px 3px}

/* timeline */
.line{position:absolute;left:416.5px;top:480px;width:1px;height:389px;background:var(--green)}
.dot{position:absolute;left:413.5px;width:7px;height:7px;border-radius:50%;background:var(--green);box-shadow:0 0 0 1.5px var(--white)}
.card{position:absolute;width:193px;background:var(--page);border:.8px solid var(--green);border-radius:3px;padding:13px 9px 0}
.card.left{left:189px}
.card.right{left:452px}
.year{position:absolute;left:9px;top:-6.5px;width:47px;height:12px;border-radius:6px;background:var(--green);color:var(--white);font-size:9px;line-height:12px;text-align:center;box-shadow:0 1px 2px rgba(0,0,0,.15)}
.card h3{font-size:8.8px;font-weight:700;color:var(--title);line-height:11px}
.card p{margin-top:5px;font-size:6.4px;line-height:7.9px;color:#333}
.card::after{content:"";position:absolute;border:5px solid transparent}
.card.left::after{right:-10.5px;top:var(--ay);border-left:6px solid var(--green)}
.card.right::after{left:-11.5px;top:var(--ay);border-right:6px solid var(--green)}

/* footer */
.footer-wave{position:absolute;left:0;top:1015px;width:834px;height:45px}
.footer{position:absolute;left:0;top:1059px;width:834px;height:141px;background:var(--brand)}
.footer .logo{left:176px;top:13px;font-size:10px}
.f-head{position:absolute;top:12px;font-size:7.8px;font-weight:500;color:var(--white)}
.f-text{position:absolute;top:47px;font-size:5.8px;line-height:7.4px;color:#c4d0e2}
.social{position:absolute;top:44px;width:12px;height:12px;border-radius:50%;background:var(--white)}
.f-rule{position:absolute;left:176px;top:103px;width:482px;height:.6px;background:#8ea3c3}
.legal{position:absolute;top:114px;font-size:5.2px;line-height:6.2px;color:var(--white)}
</style>
</head>
<body>

<header class="hero">
  <div class="hero-photo" role="img" aria-label="Aerial photograph of a hazy city skyline with high-rise towers along a river and mountains behind"></div>
  <svg class="hero-wave" viewBox="0 0 834 44" preserveAspectRatio="none" aria-hidden="true">
    <path d="M0 0 C150 0 260 44 417 44 C574 44 684 0 834 0 L834 44 L0 44 Z" fill="#f8f8f8"/>
  </svg>
  <h1 class="hero-title"><span class="accent">We are</span> a modern recruitment company,<br>powered by intelligent data, workflow, and<br>relentless people</h1>
</header>

<nav class="nav">
  <div class="logo">VANTIRA</div>
  <span class="nav-link" style="left:185px">Home</span>
  <span class="nav-link" style="left:217px">How we work</span>
  <span class="nav-link" style="left:259px">Browse jobs</span>
  <span class="nav-link" style="left:302px">Employers</span>
  <span class="nav-link active" style="left:345px">About us</span>
  <span class="nav-divider"></span>
  <span class="nav-link" style="left:401px"><span class="login-dot"></span>Login</span>
  <span class="btn-register" style="left:429px;top:7px;width:41px;height:13px"><span class="doc"></span>Register</span>
</nav>

<div class="tab" style="left:176px;width:160px">Who we are</div>
<div class="tab" style="left:337px;width:159px">Our team</div>
<div class="tab active" style="left:497px;width:161px">How we grew</div>
<section class="panel"></section>

<div class="line"></div>
<span class="dot" style="top:477px"></span>
<span class="dot" style="top:555px"></span>
<span class="dot" style="top:639px"></span>
<span class="dot" style="top:711px"></span>
<span class="dot" style="top:787px"></span>
<span class="dot" style="top:866px"></span>

<article class="card left" style="top:439px;height:70px;--ay:29px">
  <span class="year">2012</span>
  <h3>Building top talent pool</h3>
  <p>Established initially as a career development company. We worked with top schools, investment banks, management consulting, Big4 in sourcing and developing talents.</p>
</article>
<article class="card right" style="top:515px;height:85px;--ay:37px">
  <span class="year">2014</span>
  <h3>Hedge fund recruitment</h3>
  <p>Launched hedge fund recruitment in Hong Kong. We worked directly with key decision makers to hire across all roles. While hedge funds became our primary clients, we continued to also work with family offices and private equity funds.</p>
</article>
<article class="card left" style="top:607px;height:70px;--ay:29px">
  <span class="year">2015</span>
  <h3>Expanded to Singapore</h3>
  <p>As we expanded to work on Singapore based roles, we also started deepening our quant and technology talent pool to meet increasing demand from employers.</p>
</article>
<article class="card right" style="top:683px;height:60px;--ay:25px">
  <span class="year">2016</span>
  <h3>Recruiting for principal trading firms</h3>
  <p>Commenced working with systematic trading firms in hiring for quants, developers &amp; data scientists.</p>
</article>
<article class="card left" style="top:749px;height:75px;--ay:32px">
  <span class="year">2018</span>
  <h3>Recruiting for digital asset trading firms</h3>
  <p>Commenced working with digital asset trading firms. Since then, we have successfully matched talents from traditional institutions into newly created roles in fast growing fintech companies.</p>
</article>
<article class="card right" style="top:831px;height:82px;--ay:34px">
  <span class="year">2020</span>
  <h3>Present and where we are headed</h3>
  <p>Preferred recruitment partner by global hedge funds and principal trading firms in Asia for investment and technology related hires. Building onto our early success with FinTech companies, we are expanding our offering for FinTech employers in scale-up phase.</p>
</article>

<svg class="footer-wave" viewBox="0 0 834 45" preserveAspectRatio="none" aria-hidden="true">
  <path d="M0 44 C150 44 260 0 417 0 C574 0 684 44 834 44 L834 45 L0 45 Z" fill="#5874a0"/>
</svg>
<footer class="footer">
  <div class="logo">VANTIRA</div>
  <div class="f-head" style="left:337px">Talents</div>
  <div class="f-head" style="left:409px">Employers</div>
  <div class="f-head" style="left:482px">About us</div>
  <div class="f-head" style="left:554px">Connect with us</div>
  <p class="f-text" style="left:176px;width:138px">VANTIRA is a modern recruitment partner for high potential technology and finance talents. We work closely with hedge funds, systematic trading Fin Tech employers experiencing hyper growth in Asia</p>
  <p class="f-text" style="left:337px">How we work<br>Browse jobs</p>
  <p class="f-text" style="left:409px">Why VANTIRA</p>
  <p class="f-text" style="left:482px">About VANTIRA<br>Working at VANTIRA</p>
  <span class="social" style="left:554px"></span>
  <span class="social" style="left:576px"></span>
  <span class="social" style="left:598px"></span>
  <span class="btn-register" style="left:619px;top:44px;width:38px;height:12px"><span class="doc"></span>Register</span>
  <div class="f-rule"></div>
  <p class="legal" style="left:176px">@VANTIRA 2012-2020 All rights reserved.</p>
  <p class="legal" style="left:337px;width:150px">Harbourline Talent Limited (EA License No. 40217) Suite 12, Level 5, Tower 2, 88 Marina Quay Road, Kowloon Bay, Hong Kong</p>
  <p class="legal" style="left:498px;width:140px">Vantira Pte. Ltd. (License No. 19C4402) 42 Keppel Row, #11-07 Quayside Centre, Singapore 049381</p>
</footer>

</body>
</html>
```